Business Card for Wellness Clinic

We need a business card for our new logo. I want it to match the feel of the logo

Target Market(s)

Young professional families looking for holistic health care

Industry/Entity Type

Health And Wellness

Contact Information for Business Card

Our business Name: Brackenfield Health & wellness Centre, our phone #, email address...see attached old business card

Font styles to use
Sans Serif

Colors
33b8a4
cee9f5

Requirements
Must have
• my logo and business name
• Font is "Helvetica Neue LT Std 45 Light" and
• Only for "&" using font "Trajan pro bold"
• Use colors in the logo

```html
<!DOCTYPE html>
<html lang="en">
<head>
<meta charset="utf-8">
<title>Brackenfield Health &amp; Wellness Centre – Business Card</title>
<link rel="stylesheet" href="https://fonts.googleapis.com/css2?family=Work+Sans:wght@300;400&display=swap">
<style>
  :root {
    --teal: #33b8a4;
    --teal-deep: #24b09c;
    --teal-light: #3fc9b5;
    --grey-text: #9a9a9a;
    --paper: #ffffff;
    --backdrop: #d9d9d9;
    --shadow: rgba(0, 0, 0, 0.18);
  }
  * { box-sizing: border-box; margin: 0; padding: 0; }
  html, body {
    width: 1200px;
    height: 800px;
    overflow: hidden;
    background: var(--backdrop);
    font-family: "Work Sans", "Helvetica Neue", Arial, sans-serif;
    font-weight: 300;
  }
  .stage {
    width: 1200px;
    height: 800px;
    display: flex;
    flex-direction: column;
    align-items: center;
    justify-content: center;
    gap: 40px;
  }
  .card {
    position: relative;
    width: 600px;
    height: 343px;
    background: var(--paper);
    box-shadow: 0 3px 10px var(--shadow);
    overflow: hidden;
  }

  /* Wordmark */
  .wordmark {
    display: flex;
    align-items: center;
    gap: 12px;
    color: var(--grey-text);
    font-weight: 300;
    letter-spacing: 0.22em;
    text-transform: uppercase;
    line-height: 1.35;
  }
  .wordmark-square {
    flex: none;
    background: var(--teal);
  }

  /* Front */
  .card-front .wordmark {
    position: absolute;
    left: 50%;
    top: 118px;
    transform: translateX(-50%);
    font-size: 19px;
    white-space: nowrap;
  }
  .card-front .wordmark-square { width: 46px; height: 46px; }
  .card-front .front-band {
    position: absolute;
    left: 0; right: 0;
    bottom: 0;
    height: 34px;
    background: linear-gradient(90deg, var(--teal-light), var(--teal-deep));
  }

  /* Back */
  .card-back .wordmark {
    position: absolute;
    right: 28px;
    top: 26px;
    font-size: 12px;
  }
  .card-back .wordmark-square { width: 30px; height: 30px; }
  .practitioner {
    position: absolute;
    left: 32px;
    top: 96px;
  }
  .practitioner-name {
    color: var(--teal);
    font-size: 22px;
    font-weight: 300;
  }
  .practitioner-title {
    color: var(--grey-text);
    font-size: 18px;
    font-weight: 300;
    margin-top: 2px;
  }
  .contact-band {
    position: absolute;
    left: 0; right: 0;
    top: 168px;
    height: 150px;
    background: linear-gradient(90deg, var(--teal-light), var(--teal-deep));
    color: var(--paper);
    display: flex;
    justify-content: space-between;
    padding: 22px 32px 0;
  }
  .contact-list, .address {
    list-style: none;
    font-size: 16px;
    font-weight: 300;
  }
  .contact-list li {
    display: flex;
    align-items: center;
    gap: 10px;
    height: 34px;
  }
  .icon {
    width: 16px;
    height: 16px;
    flex: none;
  }
  .address {
    display: flex;
    gap: 8px;
    line-height: 1.35;
  }
  .address .icon { margin-top: 3px; }
</style>
</head>
<body>
<main class="stage">

  <section class="card card-front" aria-label="Business card front">
    <div class="wordmark">
      <span class="wordmark-square" aria-hidden="true"></span>
      <span>Brackenfield Health &amp;<br>Wellness Centre</span>
    </div>
    <div class="front-band"></div>
  </section>

  <section class="card card-back" aria-label="Business card back">
    <div class="wordmark">
      <span class="wordmark-square" aria-hidden="true"></span>
      <span>Brackenfield Health &amp;<br>Wellness Centre</span>
    </div>

    <div class="practitioner">
      <p class="practitioner-name">Dr. Maren Holt, N.D.</p>
      <p class="practitioner-title">Naturopathic Doctor</p>
    </div>

    <div class="contact-band">
      <ul class="contact-list">
        <li>
          <svg class="icon" viewBox="0 0 16 16" aria-hidden="true">
            <rect x="4" y="1" width="8" height="14" rx="1.5" fill="none" stroke="#fff" stroke-width="1.6"/>
            <circle cx="8" cy="12.5" r="0.9" fill="#fff"/>
          </svg>
          <span>613 555 0142</span>
        </li>
        <li>
          <svg class="icon" viewBox="0 0 16 16" aria-hidden="true">
            <rect x="1" y="3.5" width="14" height="9.5" rx="1" fill="none" stroke="#fff" stroke-width="1.5"/>
            <path d="M1.5 4.5 L8 9 L14.5 4.5" fill="none" stroke="#fff" stroke-width="1.5"/>
          </svg>
          <span>mholt@brackenfieldnd.ca</span>
        </li>
        <li>
          <svg class="icon" viewBox="0 0 16 16" aria-hidden="true">
            <circle cx="8" cy="8" r="6.5" fill="none" stroke="#fff" stroke-width="1.4"/>
            <ellipse cx="8" cy="8" rx="2.8" ry="6.5" fill="none" stroke="#fff" stroke-width="1.2"/>
            <path d="M1.5 8 H14.5 M2.6 4.7 H13.4 M2.6 11.3 H13.4" stroke="#fff" stroke-width="1.1"/>
          </svg>
          <span>www.brackenfieldnd.ca</span>
        </li>
      </ul>

      <div class="address">
        <svg class="icon" viewBox="0 0 16 16" aria-hidden="true">
          <path d="M8 1 C5 1 3 3.2 3 6 C3 9.5 8 15 8 15 C8 15 13 9.5 13 6 C13 3.2 11 1 8 1 Z" fill="#fff"/>
          <circle cx="8" cy="6" r="2" fill="var(--teal)"/>
        </svg>
        <p>48 Alder Row,<br>Unit 7, Linwood<br>ON L9T 4B2</p>
      </div>
    </div>
  </section>

</main>
</body>
</html>
```